The Perfect Business Card for PineHarbor

I am looking for a business card which beautifully incorporates my logo, reflects my business and looks special, elegant and clean.

```html
<!DOCTYPE html>
<html lang="en">
<head>
<meta charset="utf-8">
<title>PineHarbor Business Card</title>
<link rel="stylesheet" href="https://fonts.googleapis.com/css2?family=Marcellus&family=Philosopher&family=Roboto:wght@300&display=swap">
<style>
  :root {
    --backdrop: #2b2b2b;
    --card: #f1f1f0;
    --green: #5a7a2c;
    --green-dark: #3f5a1c;
    --ink: #4a5a36;
  }
  * { box-sizing: border-box; margin: 0; padding: 0; }
  html, body { width: 1200px; height: 1138px; overflow: hidden; }
  body { background: var(--backdrop); position: relative; font-family: "Roboto", sans-serif; }

  .card {
    position: absolute;
    background: var(--card);
    border-radius: 16px;
    overflow: hidden;
  }
  .card--front { left: 272px; top: 184px; width: 622px; height: 376px; }
  .card--back  { left: 274px; top: 606px; width: 619px; height: 375px; }

  .brand { position: absolute; display: flex; align-items: center; gap: 14px; }
  .brand__mark {
    border: 2px solid var(--green);
    border-radius: 50%;
    flex: none;
  }
  .brand__name {
    font-family: "Marcellus", serif;
    color: var(--green);
    font-weight: 400;
    letter-spacing: 0.5px;
    line-height: 1;
  }

  .card--front .brand { left: 104px; top: 120px; }
  .card--front .brand__mark { width: 104px; height: 104px; }
  .card--front .brand__name { font-size: 54px; }

  .front__web {
    position: absolute; left: 0; right: 0; top: 322px;
    text-align: center; font-weight: 300; font-size: 16px; color: var(--ink);
  }
  .front__band {
    position: absolute; left: 0; right: 0; bottom: 0; height: 14px;
    background: var(--green);
  }

  .card--back .brand { left: 246px; top: 48px; }
  .card--back .brand__mark { width: 92px; height: 92px; }
  .card--back .brand__name { font-size: 46px; }

  .back__rule { position: absolute; left: 0; top: 0; }

  .contact { position: absolute; left: 36px; top: 274px; list-style: none; }
  .contact__item {
    display: flex; align-items: center; gap: 12px;
    height: 24px; font-weight: 300; font-size: 17px; color: var(--ink);
  }
  .contact__icon { width: 16px; height: 16px; flex: none; }

  .holder {
    position: absolute; right: 27px; top: 320px;
    font-family: "Philosopher", sans-serif; font-size: 26px; color: var(--green-dark);
  }
</style>
</head>
<body>
  <section class="card card--front">
    <div class="brand">
      <span class="brand__mark"></span>
      <span class="brand__name">PineHarbor</span>
    </div>
    <p class="front__web">www.pineharborlive.com</p>
    <div class="front__band"></div>
  </section>

  <section class="card card--back">
    <div class="brand">
      <span class="brand__mark"></span>
      <span class="brand__name">PineHarbor</span>
    </div>

    <svg class="back__rule" width="619" height="375" viewBox="0 0 619 375" aria-hidden="true">
      <path d="M30 256 H278 C300 256 304 276 326 276 H590" fill="none" stroke="var(--green)" stroke-width="1.2"/>
    </svg>

    <ul class="contact">
      <li class="contact__item">
        <svg class="contact__icon" viewBox="0 0 16 16" aria-hidden="true">
          <path d="M2 5 C2 2 14 2 14 5 L12 6 L11 4.5 H5 L4 6 Z M4 7 H12 L13 13 H3 Z" fill="var(--green)"/>
        </svg>
        000-0000-0000
      </li>
      <li class="contact__item">
        <svg class="contact__icon" viewBox="0 0 16 16" aria-hidden="true">
          <rect x="1.5" y="3.5" width="13" height="9" fill="var(--green)"/>
          <path d="M1.5 3.5 L8 9 L14.5 3.5" fill="none" stroke="var(--card)" stroke-width="1.2"/>
        </svg>
        maren@pineharborlive.com
      </li>
      <li class="contact__item">
        <svg class="contact__icon" viewBox="0 0 16 16" aria-hidden="true">
          <circle cx="8" cy="8" r="6.5" fill="var(--green)"/>
          <path d="M1.5 8 H14.5 M8 1.5 V14.5 M8 1.5 C4 5 4 11 8 14.5 M8 1.5 C12 5 12 11 8 14.5" fill="none" stroke="var(--card)" stroke-width="0.9"/>
        </svg>
        www.pineharborlive.com
      </li>
    </ul>

    <p class="holder">Maren Holloway</p>
  </section>
</body>
</html>
```